Anzeigengestaltung für Unternehmensberatung für Pflegedienste
Zielgruppe
Wir sind eine Unternehmensberatung für Pflegedienste. Es soll eine Werbeanzeige erstellt werden, mit welcher schlecht laufende Pflegedienste, die gerade in einer Krise stecken angesprochen werden,
Der slogan soll einfach klingen : Pflege neu gedaxht: wirtschaftlich, nachhaltig, zukunftssicher
Anzeige in 3 Formaten
1. Format 55.3 mm x 118 mm
2. Format 1/ halbe Seite Quer 176 x 118 mm un
3. Format d 1 x A4 _Seite
Der Name der Firma Keltor GmbH info at keltor.de Tel 0381 72958143 aus Rostock Berlin und bundesweit tätig
Aufgabenstellung
Kreativ und elegant

```html
<!DOCTYPE html>
<html lang="de">
<head>
<meta charset="utf-8">
<title>Keltor GmbH – Anzeige</title>
<link href="https://fonts.googleapis.com/css2?family=Inter:wght@400;500;600&display=swap" rel="stylesheet">
<style>
  :root {
    --stage: #dfe6eb;
    --card: #ffffff;
    --navy: #1f3357;
    --ink: #1c1c1c;
    --teal: #3e6a86;
    --figure-light: #b3c9d9;
    --figure-mid: #8fadc4;
    --gold: #b99a5a;
  }
  * { margin: 0; padding: 0; box-sizing: border-box; }
  html, body {
    width: 1200px;
    height: 900px;
    overflow: hidden;
    background: var(--stage);
    font-family: "Inter", Arial, sans-serif;
  }
  .ad {
    position: absolute;
    left: 360px;
    top: 60px;
    width: 480px;
    height: 780px;
    background: var(--card);
    box-shadow: 0 10px 30px rgba(30, 50, 70, 0.18);
  }
  .brand {
    position: absolute;
    right: 40px;
    top: 48px;
    font-size: 40px;
    font-weight: 600;
    letter-spacing: 4px;
    color: var(--navy);
  }
  .headline {
    position: absolute;
    left: 0;
    right: 0;
    top: 168px;
    text-align: center;
    font-size: 27px;
    font-weight: 400;
    line-height: 1.38;
    color: var(--ink);
  }
  .visual {
    position: absolute;
    left: 82px;
    top: 310px;
    width: 316px;
    height: 245px;
    border-radius: 40px;
    background: radial-gradient(ellipse at 50% 55%, var(--figure-light) 0%, var(--figure-mid) 55%, #ffffff 100%);
  }
  .subline {
    position: absolute;
    left: 40px;
    right: 40px;
    top: 616px;
    text-align: center;
    font-size: 12.5px;
    line-height: 1.5;
    color: var(--teal);
  }
  .contact {
    position: absolute;
    left: 0;
    right: 0;
    top: 718px;
    text-align: center;
    font-size: 13px;
    color: var(--ink);
  }
</style>
</head>
<body>
  <article class="ad">
    <div class="brand">KELTOR</div>
    <h1 class="headline">Pflege neu gedacht:<br>wirtschaftlich, nachhaltig,<br>zukunftssicher</h1>
    <div class="visual" role="img" aria-label="Illustration: vier hellblaue, miteinander verbundene Figuren mit zwei goldenen Kugeln als Symbol für Zusammenhalt"></div>
    <p class="subline">Reimagining care: economical, sustainable, secure for the future.<br>Fresh structures and clear numbers for your care service.<br>Stable, feasible, secure for the future.</p>
    <p class="contact">info@keltor.de | Tel 0381 72958143 Berlin | Rostock &amp; nationwide</p>
  </article>
</body>
</html>
```